Web Design Project

We need a web site design for a new company based in New York/New Jersey called "The Lumenfold Group". We develop innovative strategies for marketing, strategic planning, business development, public relations in economic development. Simply put we create innovative strategies for invigorating smarter and stronger leaders and companies. We are a consulting firm with bold ideas for affecting change. We want to communicate that partnering with The Lumenfold Group your first decision to breakthrough innovation.

Target Market(s)

The target audience for the consulting services are private companies, economic development organizations, government and other interested in community investment strategies globally.

Industry/Entity Type

Business

Font styles to use
Serif
Sans Serif

Requirements
Must have
Nice to have
Should not have

```html
<!DOCTYPE html>
<html lang="en">
<head>
<meta charset="utf-8">
<title>The Lumenfold Group</title>
<link href="https://fonts.googleapis.com/css2?family=Ubuntu:wght@400;500&family=PT+Serif&family=Arimo&display=swap" rel="stylesheet">
<style>
:root{
  --blue:#1a73b3;
  --blue-dark:#11609e;
  --accent:#3a9bd2;
  --ink:#3b3b3b;
  --muted:#8a8a8a;
  --grey-band:#f2f3f5;
  --pale-band:#f5f7fa;
  --white:#ffffff;
}
*{margin:0;padding:0;box-sizing:border-box}
html,body{width:779px;height:1200px;overflow:hidden;background:var(--white)}
body{position:relative;font-family:'Arimo',Arial,sans-serif;color:var(--ink)}
.abs{position:absolute}
.header-band{left:0;top:0;width:779px;height:284px;background:linear-gradient(160deg,#1f80c2 0%,#176fb0 55%,#1b7cbf 100%)}
.top-nav{left:0;top:0;width:779px;height:36px;display:flex;justify-content:center;align-items:center;border-bottom:1px solid rgba(255,255,255,.08)}
.top-nav a{font-family:'Ubuntu',sans-serif;font-size:10px;color:var(--white);text-decoration:none;padding:0 21px;border-right:1px dashed rgba(255,255,255,.35);line-height:14px}
.top-nav a:last-child{border-right:none}
.brand{left:86px;top:50px;display:flex;align-items:center;gap:9px}
.brand-mark{width:44px;height:44px;border-radius:50%;background:var(--white)}
.brand-name{font-family:'Ubuntu',sans-serif;color:var(--white);line-height:1}
.brand-name .small{font-size:12.5px;display:block;margin-bottom:3px}
.brand-name .big{font-size:19px;font-weight:500}
.search{left:518px;top:63px;width:175px;height:23px;background:var(--white);border-radius:12px;font-size:7.5px;color:#666;padding:8px 0 0 15px}
.search svg{position:absolute;right:14px;top:6px}
.slider{left:86px;top:118px;width:609px;height:284px;background:var(--white);border:1px solid #d8dde2;box-shadow:0 14px 18px -10px rgba(0,0,0,.35)}
.slide-photo{left:9px;top:8px;width:589px;height:266px;background:linear-gradient(90deg,#c9d2da 0%,#e8ecef 35%,#f3efe9 55%,#e3e1dc 75%,#6f6e70 100%)}
.slide-arrows{left:24px;top:245px;display:flex;gap:2px}
.slide-arrows span,.svc-arrows span{width:16px;height:16px;background:rgba(120,120,120,.55);color:#fff;font-size:10px;display:flex;align-items:center;justify-content:center}
.welcome{left:86px;top:445px;width:410px}
.welcome h1{font-family:'Ubuntu',sans-serif;font-weight:500;font-size:17px;line-height:21px;color:#444}
.welcome h1 span{color:var(--accent);display:block}
.welcome p{font-size:7px;line-height:14px;color:var(--muted);margin-top:14px}
.newsletter{left:510px;top:449px;width:184px;height:141px;background:var(--blue);border-radius:2px;padding:11px 10px}
.newsletter h2{font-family:'Ubuntu',sans-serif;font-weight:500;font-size:16px;color:var(--white)}
.field{height:23px;border:1px solid rgba(255,255,255,.8);margin-top:10px;font-size:7px;color:var(--white);padding:7px 7px}
.field:first-of-type{margin-top:10px}
.subscribe{position:absolute;right:10px;bottom:12px;width:72px;height:23px;background:var(--white);color:var(--blue);font-family:'Ubuntu',sans-serif;font-size:8.5px;display:flex;align-items:center;justify-content:center}
.services-band{left:0;top:613px;width:779px;height:198px;background:var(--grey-band);border-top:1px solid #e3e5e8}
.services-title{left:86px;top:628px;font-family:'Ubuntu',sans-serif;font-weight:500;font-size:16px;color:#444}
.services-title span,.clients-title span{color:var(--accent)}
.svc-arrows{left:668px;top:631px;display:flex;gap:1px}
.svc-arrows span{width:12px;height:12px;font-size:8px}
.service{top:672px;width:140px;text-align:center}
.service .icon{width:69px;height:69px;margin:0 auto;border-radius:50%;background:var(--blue);border:2px solid var(--white);box-shadow:0 0 0 1.5px var(--blue);display:flex;align-items:center;justify-content:center}
.service h3{font-family:'Ubuntu',sans-serif;font-weight:400;font-size:8.5px;color:#333;margin-top:14px}
.service p{font-size:7px;line-height:13.5px;color:var(--muted);margin-top:8px}
.clients-band{left:0;top:811px;width:779px;height:237px;background:var(--pale-band);border-bottom:1px solid #e6e8eb}
.quote-mark{left:365px;top:828px;width:48px;height:48px;border-radius:50%;border:2px solid var(--blue);color:var(--blue);font-family:'PT Serif',serif;font-size:32px;font-weight:bold;text-align:center;line-height:54px}
.clients-title{left:0;top:892px;width:779px;text-align:center;font-family:'Ubuntu',sans-serif;font-weight:500;font-size:16px;color:#444}
.rule{left:110px;width:562px;height:1px;background:#dcdfe3}
.quote-text{left:110px;top:938px;width:562px;text-align:center;font-family:'PT Serif',serif;font-size:7.5px;line-height:16px;color:var(--muted)}
.quote-name{left:0;top:988px;width:779px;text-align:center;font-family:'PT Serif',serif;font-size:12.5px;color:var(--accent)}
.quote-arrows{left:366px;top:1018px;display:flex;gap:6px}
.quote-arrows span{width:19px;height:19px;border-radius:50%;border:1px solid #c4c8cc;color:#aaa;font-size:10px;display:flex;align-items:center;justify-content:center}
.footer{left:0;top:1071px;width:779px;height:129px;background:var(--blue-dark)}
.social{left:286px;top:1092px;display:flex;gap:6.5px}
.social span{width:24px;height:24px;border-radius:50%;background:var(--white)}
.footer-rule{left:86px;top:1131px;width:608px;height:1px;background:rgba(255,255,255,.15)}
.footer-nav{left:0;top:1142px;width:779px;display:flex;justify-content:center;font-size:7px;color:var(--white)}
.footer-nav span.sep{padding:0 10px}
.copyright{left:0;top:1167px;width:779px;text-align:center;font-size:7px;color:var(--white)}
</style>
</head>
<body>
<div class="abs header-band"></div>
<nav class="abs top-nav">
  <a>HOME</a><a>ABOUT US</a><a>CONSULTING</a><a>SERVICES</a><a>BLOG</a><a>TESTIMONIALS</a><a>CONTACT US</a>
</nav>
<div class="abs brand">
  <div class="brand-mark"></div>
  <div class="brand-name"><span class="small">THE LUMENFOLD</span><span class="big">GROUP</span></div>
</div>
<div class="abs search">SEARCH
  <svg width="10" height="10" viewBox="0 0 10 10"><circle cx="4" cy="4" r="3" fill="none" stroke="#555" stroke-width="1.5"/><line x1="6.2" y1="6.2" x2="9" y2="9" stroke="#555" stroke-width="1.8"/></svg>
</div>

<div class="abs slider">
  <div class="abs slide-photo" role="img" aria-label="Photo of a confident businesswoman standing in front of blurred colleagues in a bright office"></div>
  <div class="abs slide-arrows"><span>&#8249;</span><span>&#8250;</span></div>
</div>

<section class="abs welcome">
  <h1>WELCOME TO <span>THE LUMENFOLD GROUP</span></h1>
  <p>Sed ut perspiciatis unde omnis iste natus error sit voluptatem accusantium doloremque laudantium, totam rem aperiam, eaque ipsa quae ab illo inventore veritatis et quasi architecto beatae vitae dicta sunt explicabo. Nemo enim ipsam voluptatem quia sed quia consequuntur magni dolores eos qui ratione voluptatem sequi nesciunt.</p>
  <p>Neque porro quisquam est, qui dolorem ipsum quia dolor sit amet, consectetur, adipisci velit, sed quia non numquam eius modi tempora incidunt ut labore et dolore magnam aliquam quaerat voluptatem. Ut enim ad minima veniam, quis nostrum exercitationem ullam corporis suscipit laboriosam, nisi ut aliquid sequi nesciunt.</p>
</section>

<aside class="abs newsletter">
  <h2>NEWSLETTER</h2>
  <div class="field">Enter Your Email :</div>
  <div class="field">Enter Your Password :</div>
  <div class="subscribe">SUBSCRIBE</div>
</aside>

<div class="abs services-band"></div>
<h2 class="abs services-title">OUR <span>SERVICES</span></h2>
<div class="abs svc-arrows"><span>&#8249;</span><span>&#8250;</span></div>

<div class="abs service" style="left:88px">
  <div class="icon"><svg width="38" height="30" viewBox="0 0 38 30"><g fill="#fff"><rect x="2" y="14" width="6" height="14"/><rect x="11" y="10" width="6" height="18"/><rect x="20" y="12" width="6" height="16"/><rect x="29" y="6" width="6" height="22"/></g><polyline points="5,9 14,5 23,7 32,1" fill="none" stroke="#fff" stroke-width="1.5"/><g fill="#fff"><circle cx="5" cy="9" r="2"/><circle cx="14" cy="5" r="2"/><circle cx="23" cy="7" r="2"/><circle cx="32" cy="1.8" r="1.8"/></g></svg></div>
  <h3>STRATEGIES FOR MARKETING</h3>
  <p>Sed ut perspiciatis unde omnis iste natus error sit voluptatem accusantium dolo-remque laudantium, explicabo.</p>
</div>
<div class="abs service" style="left:242px">
  <div class="icon"><svg width="36" height="32" viewBox="0 0 36 32"><rect x="2" y="2" width="32" height="21" rx="2" fill="none" stroke="#fff" stroke-width="2"/><circle cx="11" cy="12" r="5" fill="#fff"/><g fill="#fff"><rect x="19" y="12" width="3" height="7"/><rect x="24" y="8" width="3" height="11"/><rect x="29" y="11" width="2" height="8"/></g><rect x="16" y="23" width="4" height="4" fill="#fff"/><rect x="10" y="27" width="16" height="2" fill="#fff"/></svg></div>
  <h3>STRATEGIC PLANNING</h3>
  <p>Sed ut perspiciatis unde omnis iste natus error sit voluptatem accusantium dolo-remque laudantium, explicabo.</p>
</div>
<div class="abs service" style="left:399px">
  <div class="icon"><svg width="38" height="38" viewBox="0 0 38 38"><g fill="none" stroke="#fff"><circle cx="13" cy="13" r="6" stroke-width="5" stroke-dasharray="3 2.3"/><circle cx="25" cy="25" r="8" stroke-width="6" stroke-dasharray="3.5 2.6"/></g><circle cx="25" cy="25" r="2.5" fill="#1a73b3"/></svg></div>
  <h3>BUSINESS DEVELOPMENT</h3>
  <p>Sed ut perspiciatis unde omnis iste natus error sit voluptatem accusantium dolo-remque laudantium, explicabo.</p>
</div>
<div class="abs service" style="left:554px">
  <div class="icon"><svg width="44" height="26" viewBox="0 0 44 26"><g fill="#fff"><rect x="1" y="3" width="6" height="16"/><rect x="37" y="3" width="6" height="16"/><path d="M8 5 L18 4 L26 8 L20 11 L16 9 L12 11 L22 20 L18 22 L8 16 Z"/><path d="M36 5 L28 4 L22 7 L30 12 L34 17 L28 22 L24 19 L36 16 Z"/></g></svg></div>
  <h3>PUBLIC RELATIONS</h3>
  <p>Sed ut perspiciatis unde omnis iste natus error sit voluptatem accusantium dolo-remque laudantium, explicabo.</p>
</div>

<div class="abs clients-band"></div>
<div class="abs quote-mark">&#8220;</div>
<h2 class="abs clients-title">WHAT OUR <span>CLIENTS SAYING</span></h2>
<div class="abs rule" style="top:930px"></div>
<p class="abs quote-text">Giving children a voice in decisions that shape their lives is not only their right, but leads to better outcomes in development programmes. We helped Brightwater Relief and a consortium of INGOs develop a digital strategy to get child participation back on the map.</p>
<div class="abs rule" style="top:979px"></div>
<div class="abs quote-name">Elena Marsh</div>
<div class="abs quote-arrows"><span>&#8249;</span><span>&#8250;</span></div>

<footer class="abs footer"></footer>
<div class="abs social"><span></span><span></span><span></span><span></span><span></span><span></span><span></span></div>
<div class="abs footer-rule"></div>
<div class="abs footer-nav">
  <span>HOME</span><span class="sep">/</span><span>ABOUT US</span><span class="sep">/</span><span>CONSULTING</span><span class="sep">/</span><span>SERVICES</span><span class="sep">/</span><span>BLOG</span><span class="sep">/</span><span>TESTIMONIALS</span><span class="sep">/</span><span>CONTACT US</span>
</div>
<div class="abs copyright">&copy; Copy Rights 2014 The Lumenfold Group. All Rights Reserved</div>
</body>
</html>
```